Direct Mail flyer for the timeshare industry.

We need someone who has experience in direct mail experience in postcards and successful campaigns. The post card we are using is not good at all.

We are looking at a 5.5 x 8.5 postcard with 4 color on one side and the black and white on the mailing side. But if someone has a better idea instead of a postcard then I am open to that

Target Market(s)

Timeshare owners...most of them are 55 plus in age. We help people get out of their time share

Industry/Entity Type

Industry

Font styles to use
Serif

Colors

Designer to choose colors to be used in the design.

Requirements
Must have
• Call to action and be easy to understand and look very professional and not fake or cheesy

```html
<!DOCTYPE html>
<html lang="en">
<head>
<meta charset="utf-8">
<title>HLS Group – Private Event Invitation Postcard</title>
<link rel="stylesheet" href="https://fonts.googleapis.com/css2?family=Rajdhani:wght@300;500;700&display=swap">
<style>
  :root {
    --backdrop: #65686b;
    --paper: #ffffff;
    --ink: #000000;
    --rule: #555555;
    --education: #4c74b9;
    --protection: #6cae6c;
    --advisement: #a8465a;
    --card-shadow: #1a1a1a;
  }
  * { margin: 0; padding: 0; box-sizing: border-box; }
  html, body {
    width: 960px; height: 1200px; overflow: hidden;
    background: var(--backdrop);
    font-family: "Rajdhani", "Arial Narrow", sans-serif;
    color: var(--ink);
  }
  .postcard {
    position: absolute; left: 109px;
    background: var(--paper);
    box-shadow: 9px 9px 0 var(--card-shadow);
    overflow: hidden;
  }
  .postcard--mailing { top: 90px; width: 741px; height: 480px; }
  .postcard--front { top: 630px; width: 744px; height: 482px; overflow: visible; }

  /* Mailing side */
  .return-block {
    position: absolute; left: 0; top: 0; width: 376px; height: 222px;
    border-right: 11px solid var(--ink); border-bottom: 11px solid var(--ink);
  }
  .mailing-label {
    position: absolute; left: 21px; top: 18px; width: 68px; height: 102px;
    border: 1px dotted #777;
    display: flex; align-items: center; justify-content: center; text-align: center;
    font-weight: 300; font-size: 14px; line-height: 1.25;
  }
  .address {
    position: absolute; left: 97px; top: 14px;
    font-weight: 300; font-size: 20px; line-height: 26px; text-transform: uppercase;
  }
  .address strong, .to-label { font-weight: 700; }
  .to-label { position: absolute; left: 97px; top: 92px; font-size: 20px; }
  .address-line { position: absolute; height: 1px; background: var(--rule); right: 36px; }

  .event-details {
    position: absolute; left: 416px; top: 128px; right: 0; bottom: 0;
    border-left: 11px solid var(--ink); border-top: 11px solid var(--ink);
    padding: 6px 0 0 13px;
    font-weight: 300; font-size: 21px; line-height: 26px; text-transform: uppercase;
  }
  .event-details .label { font-weight: 700; font-style: italic; }
  .event-details .venue { font-weight: 700; }
  .event-details .cta { margin-top: 8px; }
  .event-details .cta strong { font-weight: 700; }
  .rsvp {
    position: absolute; left: 446px; top: 406px; right: 0; bottom: 0;
    border-left: 11px solid var(--ink); border-top: 11px solid var(--ink);
    background: var(--paper);
    padding: 18px 0 0 23px;
    font-weight: 300; font-size: 21px; text-transform: uppercase;
  }
  .rsvp strong { font-weight: 700; }

  /* Front side */
  .invite-frame {
    position: absolute; left: 418px; top: 16px; width: 329px; height: 432px;
    z-index: 1;
    background: var(--paper);
    border: 11px solid var(--ink);
    padding: 8px 35px 0 0; text-align: right; text-transform: uppercase;
  }
  .invite-title { font-weight: 700; font-size: 42px; line-height: 42px; }
  .invite-sub { font-weight: 300; font-size: 42px; line-height: 42px; }
  .invite-body { margin-top: 10px; font-weight: 300; font-size: 21px; line-height: 23.3px; }
  .invite-body strong { font-weight: 700; }

  .benefit {
    position: absolute; z-index: 2; width: 407px; color: var(--paper);
    padding: 10px 0 0 19px; text-transform: uppercase;
    box-shadow: 2px 2px 10px rgba(0,0,0,0.35);
  }
  .benefit h2 { font-weight: 700; font-size: 42px; line-height: 40px; margin-bottom: 2px; }
  .benefit p { font-weight: 300; font-size: 20px; line-height: 17px; white-space: nowrap; }
  .benefit--education { left: 43px; top: 43px; height: 439px; background: var(--education); z-index: 2; }
  .benefit--protection { left: 73px; top: 177px; height: 305px; background: var(--protection); z-index: 3; }
  .benefit--advisement { left: 102px; top: 327px; height: 155px; background: var(--advisement); z-index: 4; }
</style>
</head>
<body>

<section class="postcard postcard--mailing" aria-label="Mailing side">
  <div class="return-block">
    <div class="mailing-label">MAILING<br>LABEL</div>
    <p class="address"><strong>From:</strong> HLS Group, LLC<br>2210 W Maple Ridge Road<br>Oakfield, MO. 65012</p>
    <span class="to-label">TO:</span>
    <span class="address-line" style="left:137px; top:115px;"></span>
    <span class="address-line" style="left:97px; top:139px;"></span>
    <span class="address-line" style="left:97px; top:163px;"></span>
    <span class="address-line" style="left:97px; top:187px;"></span>
  </div>

  <div class="event-details">
    <p class="label">Where?</p>
    <p class="venue">Lakeside Conference Hotel</p>
    <p>1200 Commerce Parkway Fort<br>Worth, TX 76100</p>
    <p class="label">When?</p>
    <p>Day, Date, Year</p>
    <p>Time | Time | Time</p>
    <p class="cta">Call <strong>(888) 555-0142</strong> today<br>to guarantee your seats!</p>
  </div>

  <div class="rsvp"><strong>RSVP</strong> Code # HLS00001</div>
</section>

<section class="postcard postcard--front" aria-label="Invitation side">
  <div class="invite-frame">
    <p class="invite-title">A Private<br>Event<br>Invitation</p>
    <p class="invite-sub">Limited<br>Seating</p>
    <p class="invite-body">This is your<br>chance! We’ve<br>arranged for you<br>and one guest to<br>attend our HLS<br>Group event<br><strong>Free of charge</strong></p>
  </div>

  <div class="benefit benefit--education">
    <h2>Education</h2>
    <p>We promise this event will be an eye-<br>opening experience and an incredible<br>learning opportunity regardless of<br>your current situation.</p>
  </div>
  <div class="benefit benefit--protection">
    <h2>Protection</h2>
    <p>Arm yourself with the knowledge<br>of how to avoid<br>the current scams occurring in the<br>timeshare industry to<br>protect you as an owner.</p>
  </div>
  <div class="benefit benefit--advisement">
    <h2>Advisement</h2>
    <p>Your questions are welcomed and<br>will be addressed. This will bring<br>you the sense of<br>confidence that you have been<br>seeking.</p>
  </div>
</section>

</body>
</html>
```